Digital Album Cover for a Christmas Song

We are looking for someone to design us a digital album cover for a Christmas track which will be released in December 2018. The cover will be displayed on online music channels and streaming services such as Melorack and Plavora.

The track (attached for reference) is called "Maybe Tonight Or Maybe Never". and the artist is "Dellan Voss Group"

We are open to ideas about imagery, but would like the cover to convey the juxtaposition of this song being a Christmas track, but at the same time not sounding/being particularly festive - a contrast of two ideas. We would also like the final cover to look slightly vintage - from the 80's era.

The final submission should be 6000x6000 pixels RGB, and please supply PSD/AI working files too.

```html
<!DOCTYPE html>
<html lang="en">
<head>
<meta charset="utf-8">
<title>Maybe Tonight Or Maybe Never — Dellan Voss Group</title>
<link rel="stylesheet" href="https://fonts.googleapis.com/css2?family=Jost:wght@500;600&display=swap">
<style>
  :root {
    --backdrop: #767676;
    --cover-dark: #0c0b0b;
    --cover-deep: #141716;
    --band: #ffffff;
    --title: #c95a5c;
    --artist: #f2f2f2;
  }
  html, body {
    margin: 0;
    padding: 0;
    width: 739px;
    height: 1200px;
    overflow: hidden;
    background: var(--backdrop);
  }
  .canvas {
    position: relative;
    width: 739px;
    height: 1200px;
    display: flex;
    align-items: center;
    justify-content: center;
  }
  .album-cover {
    position: relative;
    width: 600px;
    height: 600px;
    overflow: hidden;
    font-family: "Jost", "Futura", sans-serif;
    box-shadow: 0 14px 22px rgba(0, 0, 0, 0.25);
  }
  .cover-photo {
    position: absolute;
    inset: 0;
    background:
      radial-gradient(ellipse at 30% 20%, #1d2220 0%, transparent 55%),
      radial-gradient(ellipse at 70% 85%, #1a1e1c 0%, transparent 50%),
      linear-gradient(160deg, var(--cover-deep), var(--cover-dark));
  }
  .title-band {
    position: absolute;
    left: 0;
    right: 0;
    top: 252px;
    height: 76px;
    background: var(--band);
  }
  .title-line {
    position: absolute;
    left: 0;
    right: 0;
    margin: 0;
    text-align: center;
    color: var(--title);
    font-weight: 600;
    font-size: 68px;
    line-height: 76px;
    letter-spacing: 0.5px;
    text-transform: uppercase;
  }
  .title-line--top { top: 172px; }
  .title-line--band { top: 252px; }
  .title-line--bottom { top: 332px; }
  .artist-name {
    position: absolute;
    left: 0;
    right: 0;
    top: 414px;
    margin: 0;
    text-align: center;
    color: var(--artist);
    font-weight: 500;
    font-size: 16px;
    letter-spacing: 4px;
    text-transform: uppercase;
  }
</style>
</head>
<body>
  <main class="canvas">
    <section class="album-cover">
      <div class="cover-photo" role="img" aria-label="Dark photograph of pine branches with small warm orange lights"></div>
      <div class="title-band"></div>
      <h1 class="title-line title-line--top">Maybe</h1>
      <h1 class="title-line title-line--band">Tonight Or</h1>
      <h1 class="title-line title-line--bottom">Maybe Never</h1>
      <p class="artist-name">Dellan Voss Group</p>
    </section>
  </main>
</body>
</html>
```